Business Card Design Project

Hello
I want a Simple Business card that uses the company logo that is easily reasonable but looks professional as I am an IT Services company and would look to share these cards with prospective clients.
The details are:
Kestrel Arc Solutions
14 Morrow Lane
Birmingham
B7 4QX
Telephone 0845 217 6640
I would like my name Oliver Hastings and my title Director on the card.
Target Market(s)
IT Professionals
Industry/Entity Type
Business

```html
<!DOCTYPE html>
<html lang="en">
<head>
<meta charset="utf-8">
<title>Kestrel Arc Solutions – Business Card</title>
<link rel="stylesheet" href="https://fonts.googleapis.com/css2?family=Josefin+Sans:wght@300&display=swap">
<style>
  :root {
    --card-green: #7cc354;
    --card-white: #ffffff;
    --rule-yellow: #fcd96a;
    --ink-dark: #231f20;
    --ink-light: #ffffff;
    --mark-green: #9fd06d;
  }
  html, body {
    margin: 0;
    padding: 0;
    width: 1200px;
    height: 667px;
    overflow: hidden;
    background: var(--card-green);
  }
  .business-card {
    position: relative;
    width: 1200px;
    height: 667px;
    overflow: hidden;
    background: var(--card-green);
    font-family: "Josefin Sans", "Century Gothic", sans-serif;
    font-weight: 300;
  }
  .card-shapes {
    position: absolute;
    inset: 0;
    width: 1200px;
    height: 667px;
  }
  .brand-lockup {
    position: absolute;
    left: 0;
    right: 80px;
    top: 170px;
    display: flex;
    justify-content: center;
    align-items: center;
    gap: 22px;
  }
  .brand-dot {
    width: 46px;
    height: 46px;
    border-radius: 50%;
    background: var(--mark-green);
    flex: none;
  }
  .brand-name {
    margin: 0;
    font-size: 62px;
    font-weight: 300;
    color: var(--ink-dark);
    letter-spacing: 1px;
    line-height: 1;
    white-space: nowrap;
  }
  .card-holder {
    position: absolute;
    left: 44px;
    top: 500px;
    margin: 0;
    font-size: 41px;
    color: var(--ink-light);
    letter-spacing: 0.5px;
    white-space: nowrap;
  }
  .contact-details {
    position: absolute;
    left: 635px;
    top: 470px;
    margin: 0;
    font-size: 30px;
    line-height: 33px;
    color: var(--ink-light);
    letter-spacing: 0.5px;
    font-style: normal;
  }
  .contact-details p {
    margin: 0;
  }
  .contact-details .contact-phone {
    margin-bottom: 33px;
  }
</style>
</head>
<body>
  <main class="business-card">
    <svg class="card-shapes" viewBox="0 0 1200 667" aria-hidden="true">
      <defs>
        <radialGradient id="edge-sheen" cx="0" cy="290" r="140" gradientUnits="userSpaceOnUse">
          <stop offset="0" stop-color="#ffffff" stop-opacity="0.7"/>
          <stop offset="1" stop-color="#ffffff" stop-opacity="0"/>
        </radialGradient>
      </defs>
      <rect class="sheen" x="0" y="180" width="150" height="240" fill="url(#edge-sheen)"/>
      <path class="header-panel"
            d="M0,170 C 190,330 420,405 640,403 C 880,400 1080,260 1200,40 V0 H0 Z"
            fill="var(--card-white)" stroke="var(--rule-yellow)" stroke-width="7"/>
    </svg>

    <header class="brand-lockup">
      <span class="brand-dot"></span>
      <h1 class="brand-name">Kestrel Arc Solutions</h1>
    </header>

    <p class="card-holder">Director: Oliver Hastings</p>

    <address class="contact-details">
      <p class="contact-phone">Phone Number: 0845 217 6640</p>
      <p class="contact-address">Adress: 14 Morrow Lane;<br>Birmingham; B7 4QX</p>
    </address>
  </main>
</body>
</html>
```